PaceUp

This app is built around three game modes—Quick Focus, Daily, and Calming—each offering short, low-stress interactions designed to prime focus, train cognitive skills, or regulate anxiety using neuroscience-informed mechanics. Gameplay spans spatial puzzles, word and memory challenges, and breathing or sensory experiences, all delivered in 1–5 minute routines with clean, calming UI patterns (grids, cards, breathing rings, soft animations). The goal is a cohesive system of micro-games and guided routines that enhance executive function, emotional regulation, and readiness before, during, or after high-stakes moments.

Colors
FFC000
F8CF3A
FAE287
FDF2CF
FEFAEE
F0912C
F2A743
F7CA91
FBE8D2
FDF5EE
EE7325
F08F49
F5BC92
FAE3D3
FDF4ED

```html
<!DOCTYPE html>
<html lang="en">
<head>
<meta charset="utf-8">
<title>Session Complete</title>
<link rel="stylesheet" href="https://fonts.googleapis.com/css2?family=Outfit:wght@400;500;600;700&family=Inter:wght@600&display=swap">
<style>
  :root {
    --bg: #F5ECE3;
    --band: #F6E8C6;
    --ink: #3A2E1C;
    --card: #FFFFFF;
    --tick: #67C23A;
    --btn-start: #FFA36F;
    --btn-end: #F47A1F;
    --close-chip: #F7F6F3;
    --close-icon: #3A2E1C;
  }
  * { margin: 0; padding: 0; box-sizing: border-box; }
  html, body { width: 677px; height: 1200px; overflow: hidden; }
  body { background: var(--bg); font-family: "Outfit", sans-serif; color: var(--ink); }

  .screen { position: relative; width: 677px; height: 1200px; overflow: hidden; background: var(--bg); }
  .screen__band { position: absolute; inset: 0; width: 100%; height: 100%; }

  .status-bar {
    position: absolute; top: 0; left: 0; right: 0; height: 64px;
    display: flex; align-items: center; justify-content: space-between;
    padding: 0 40px 0 52px;
  }
  .status-bar__time { font-family: "Inter", sans-serif; font-weight: 600; font-size: 20px; letter-spacing: 0.2px; }
  .status-bar__icons { display: flex; gap: 7px; align-items: center; }

  .result {
    position: absolute; top: 376px; left: 0; right: 0;
    display: flex; flex-direction: column; align-items: center;
  }
  .result__badge {
    width: 174px; height: 174px; border-radius: 42px; background: var(--card);
    display: flex; align-items: center; justify-content: center;
    box-shadow: 0 22px 22px -10px rgba(90, 70, 40, 0.22);
  }
  .result__title { margin-top: 34px; font-weight: 700; font-size: 62px; letter-spacing: -0.3px; line-height: 1.1; white-space: nowrap; }
  .result__subtitle { margin-top: 22px; font-weight: 400; font-size: 30px; line-height: 1.2; white-space: nowrap; }

  .close-button {
    position: absolute; left: 60px; top: 1014px; width: 557px; height: 86px;
    border: none; border-radius: 43px;
    background: linear-gradient(110deg, var(--btn-start) 0%, var(--btn-start) 35%, var(--btn-end) 72%);
    display: flex; align-items: center; justify-content: center;
    font-family: "Outfit", sans-serif; font-weight: 600; font-size: 24px; color: #FFFFFF;
  }
  .close-button__chip {
    position: absolute; right: 8px; top: 8px; width: 70px; height: 70px; border-radius: 50%;
    background: var(--close-chip); display: flex; align-items: center; justify-content: center;
  }
</style>
</head>
<body>
  <main class="screen">
    <svg class="screen__band" viewBox="0 0 484 1050" preserveAspectRatio="none" aria-hidden="true">
      <path d="M290 0 C360 90 375 230 335 370 C300 480 230 560 130 710 C80 785 35 850 0 905 L0 1050 L30 1050 C80 960 180 840 300 720 C380 640 440 570 484 500 L484 0 Z" fill="var(--band)"/>
    </svg>

    <header class="status-bar">
      <span class="status-bar__time">9:41</span>
      <span class="status-bar__icons">
        <svg width="22" height="14" viewBox="0 0 22 14" aria-hidden="true"><rect x="0" y="9" width="4" height="5" rx="1" fill="var(--ink)"/><rect x="6" y="6" width="4" height="8" rx="1" fill="var(--ink)"/><rect x="12" y="3" width="4" height="11" rx="1" fill="var(--ink)"/><rect x="18" y="0" width="4" height="14" rx="1" fill="var(--ink)"/></svg>
        <svg width="20" height="14" viewBox="0 0 20 14" aria-hidden="true"><path d="M10 13.5 L7 10.3 A4.5 4.5 0 0 1 13 10.3 Z" fill="var(--ink)"/><path d="M4.6 7.8 A7.8 7.8 0 0 1 15.4 7.8" stroke="var(--ink)" stroke-width="2.2" fill="none" stroke-linecap="round"/><path d="M1.5 4.6 A12 12 0 0 1 18.5 4.6" stroke="var(--ink)" stroke-width="2.2" fill="none" stroke-linecap="round"/></svg>
        <svg width="30" height="14" viewBox="0 0 30 14" aria-hidden="true"><rect x="0.75" y="0.75" width="25" height="12.5" rx="3.5" stroke="var(--ink)" stroke-opacity="0.4" stroke-width="1.5" fill="none"/><rect x="3" y="3" width="20.5" height="8" rx="2" fill="var(--ink)"/><rect x="27.5" y="4.5" width="2" height="5" rx="1" fill="var(--ink)" fill-opacity="0.4"/></svg>
      </span>
    </header>

    <section class="result">
      <div class="result__badge">
        <svg width="70" height="70" viewBox="0 0 70 70" aria-hidden="true">
          <circle cx="35" cy="35" r="35" fill="var(--tick)"/>
          <path d="M22 36 L31 44 L48 27" stroke="#FFFFFF" stroke-width="6" fill="none" stroke-linecap="round" stroke-linejoin="round"/>
        </svg>
      </div>
      <h1 class="result__title">Congratulations!</h1>
      <p class="result__subtitle">Daily session completed</p>
    </section>

    <button class="close-button" type="button">
      Close
      <span class="close-button__chip">
        <svg width="20" height="20" viewBox="0 0 20 20" aria-hidden="true"><path d="M3 3 L17 17 M17 3 L3 17" stroke="var(--close-icon)" stroke-width="2.2" stroke-linecap="round"/></svg>
      </span>
    </button>
  </main>
</body>
</html>
```